Auto Repair Specialist needs wordpress design

We are looking for a Word Press website design for a Vantor Truck Service and Repair Specialist shop called Gearhaven. The design should have a slightly retro Industrial feel. You can see our logo and an example of our sign in attached files.

```html
<!DOCTYPE html>
<html lang="en">
<head>
<meta charset="utf-8">
<title>Gearhaven, LLC — Vantor Truck Service &amp; Repair</title>
<link href="https://fonts.googleapis.com/css2?family=Krona+One&family=Poppins:wght@400;500;600&display=swap" rel="stylesheet">
<style>
:root{
  --blue:#2d3b9c;
  --blue-deep:#25318a;
  --navy:#1c2154;
  --ink:#1f2a7a;
  --grey:#8a8ea6;
  --text:#4a4d5e;
  --pale:#eef0fb;
  --white:#ffffff;
  --star:#f3c316;
  --head:"Krona One",sans-serif;
  --body:"Poppins",sans-serif;
}
*{margin:0;padding:0;box-sizing:border-box}
html,body{width:1200px;height:3328px;overflow:hidden}
body{position:relative;font-family:var(--body);color:var(--text);background:var(--white)}
.abs{position:absolute}
svg{display:block}

/* top bar + nav */
.topbar{left:0;top:0;width:1200px;height:38px;background:#23264a}
.topbar .phone{right:62px;top:8px;color:var(--white);font-size:17px;font-weight:500;display:flex;align-items:center;gap:10px}
.nav{left:0;top:38px;width:1200px;height:74px;background:var(--blue)}
.brand{display:flex;align-items:center;gap:8px;color:var(--white);font-family:var(--body);font-weight:600;font-size:18px}
.brand .dot{width:22px;height:22px;border-radius:50%;background:var(--white)}
.nav .brand{left:61px;top:24px}
.nav-links{left:0;top:28px;width:1200px;font-size:13.5px;color:var(--white)}
.nav-links span{position:absolute;transform:translateX(-50%);white-space:nowrap}
.btn-light{background:var(--white);color:var(--navy);border-radius:22px;font-size:13.5px;display:flex;align-items:center;justify-content:center}
.nav .btn-light{left:973px;top:16px;width:165px;height:38px}

/* hero */
.hero{left:0;top:112px;width:1200px;height:563px;background:linear-gradient(100deg,#4a5368 0%,#6b7690 40%,#3c4460 70%,#8b93a8 100%)}
.hero .shade{inset:0;background:rgba(20,24,50,.38)}
.hero .kicker{left:0;width:1200px;top:118px;text-align:center;font-family:var(--head);color:var(--white);font-size:17px;letter-spacing:1px}
.hero h1{left:0;width:1200px;top:150px;text-align:center;font-family:var(--head);font-weight:400;color:var(--white);font-size:52px;letter-spacing:2px}
.hero p{left:350px;width:500px;top:218px;text-align:center;color:var(--white);font-size:13px;line-height:22px}
.hero .btn-light{left:517px;top:299px;width:166px;height:38px;border:2px solid var(--blue)}
.hero .arrow{width:38px;height:38px;border-radius:50%;top:245px;display:flex;align-items:center;justify-content:center}
.hero .arrow.prev{left:42px;border:2px solid var(--white)}
.hero .arrow.next{left:1120px;background:var(--blue);width:36px;height:36px}

.band-pale{left:0;top:675px;width:1200px;height:229px;background:var(--pale)}
.card{width:339px;height:314px;top:537px;background:var(--white);border-radius:12px;text-align:center;box-shadow:0 6px 20px rgba(30,40,120,.08)}
.card.active{background:var(--blue);color:var(--white)}
.card .icon{width:94px;height:94px;border-radius:50%;border:2px solid var(--blue);margin:29px auto 0;display:flex;align-items:center;justify-content:center}
.card.active .icon{border-color:var(--white)}
.card h3{font-family:var(--head);font-weight:400;color:var(--blue);font-size:19px;margin-top:17px}
.card.active h3{color:var(--white)}
.card p{font-size:13px;line-height:20px;width:265px;margin:10px auto 0;color:var(--text)}
.card.active p{color:var(--white)}
.card .more{font-size:13px;font-weight:500;color:var(--blue);margin-top:12px;display:flex;align-items:center;justify-content:center;gap:8px}
.card.active .more{color:var(--white)}

/* about */
.about-ring{left:60px;top:989px;width:450px;height:450px;border-radius:50%;background:var(--blue)}
.about-photo{left:88px;top:1005px;width:426px;height:426px;border-radius:50%;background:linear-gradient(160deg,#c9ced8,#e9ecf1 45%,#5b6f9e 80%,#2f3d7c)}
.about h2{left:643px;top:1032px;font-family:var(--head);font-weight:400;font-size:34px;line-height:44px}
.about h2 .l1{color:var(--blue);padding-left:12px;display:block}
.about h2 .l2{color:var(--grey);display:block}
.about p{left:643px;width:485px;font-size:13px;line-height:20.2px}
.btn-blue{background:var(--blue);color:var(--white);border-radius:22px;font-size:13px;display:flex;align-items:center;justify-content:center}
.about .btn-blue{left:642px;top:1337px;width:116px;height:37px}
.about .or{left:777px;top:1343px;color:var(--blue);font-size:15px}
.about .call{left:818px;top:1334px;display:flex;align-items:center;gap:14px;color:var(--blue);font-size:18px;font-weight:500}

/* cta band */
.cta{left:0;top:1522px;width:1200px;height:283px;background:linear-gradient(100deg,#2a3796,#34419f 55%,#2b3897)}
.cta h2{left:61px;top:68px;width:680px;font-family:var(--head);font-weight:400;color:var(--white);font-size:26px;line-height:38px}
.cta p{left:61px;top:142px;width:660px;color:var(--white);font-size:13px;line-height:20.2px}
.cta .req{left:900px;top:84px;width:239px;height:105px;background:var(--white);border-radius:10px;font-family:var(--head);color:var(--blue);font-size:18px;line-height:30px;text-align:center;display:flex;align-items:center;justify-content:center}

/* reviews */
.reviews{left:0;top:1805px;width:1200px;height:452px;background:var(--pale);overflow:hidden}
.reviews h2{left:0;width:1200px;top:52px;text-align:center;font-family:var(--head);font-weight:400;font-size:35px;color:var(--blue)}
.reviews h2 span{color:var(--grey)}
.review{width:291px;height:194px;background:var(--white);border-radius:6px;padding:24px 24px 0 26px;box-shadow:0 4px 16px rgba(30,40,120,.06)}
.review .stars{display:flex;gap:5px}
.review p{font-size:13.5px;line-height:22.5px;margin-top:10px}
.review .who{font-family:var(--head);color:var(--blue);font-size:13px;margin-top:10px}
.reviews .pg{top:357px;width:33px;height:33px;border-radius:50%;display:flex;align-items:center;justify-content:center}

/* contact */
.map{left:605px;top:2257px;width:488px;height:290px;background:linear-gradient(135deg,#f3f4f7,#e7e9ee)}
.contact-title{left:192px;top:2336px;font-family:var(--head);font-weight:400;font-size:34px;line-height:42px}
.contact-title .l1{color:var(--blue);display:block}
.contact-title .l2{color:var(--grey);display:block}
.contact-box{left:189px;top:2445px;width:846px;height:375px;background:var(--white);border-radius:8px;box-shadow:0 8px 28px rgba(30,40,120,.09)}
.info{left:0;top:0;width:299px;height:375px;background:var(--blue);border-radius:8px 0 0 8px;color:var(--white)}
.info h4{left:36px;top:56px;font-family:var(--head);font-weight:400;font-size:15px}
.info .row{left:34px;display:flex;gap:16px}
.info .ico{width:40px;height:40px;border-radius:50%;border:1.5px solid var(--white);display:flex;align-items:center;justify-content:center;flex-shrink:0}
.info .lab{font-size:12px;color:#c9cdf0;letter-spacing:.5px}
.info .val{font-size:12.5px;line-height:19px;margin-top:3px}
.form h4{left:342px;top:30px;font-family:var(--head);font-weight:400;color:var(--blue);font-size:15px}
.field{height:33px;border:1px solid #cfd2dc;border-radius:3px;font-size:12.5px;color:var(--grey);padding:8px 12px}
.field.on{border-color:var(--blue)}
.form .submit{left:339px;top:295px;width:473px;height:37px;font-size:13px}

/* call band */
.callband{left:0;top:2906px;width:1200px;height:113px;background:var(--blue)}
.callband h2{left:61px;top:41px;font-family:var(--head);font-weight:400;color:var(--white);font-size:25px}
.callband .pill{left:952px;top:43px;width:187px;height:38px;background:var(--white);border-radius:20px;display:flex;align-items:center;gap:10px;padding-left:4px;color:var(--blue);font-size:16px;font-weight:500}
.callband .pill .c{width:32px;height:32px;border-radius:50%;border:1.5px solid var(--blue);display:flex;align-items:center;justify-content:center}

/* footer */
.footer{left:0;top:3019px;width:1200px;height:309px;background:var(--navy);color:var(--white)}
.footer .brand{left:61px;top:70px;font-size:24px}
.footer .blurb{left:61px;top:167px;width:240px;font-size:12.5px;line-height:21px}
.footer h5{font-family:var(--head);font-weight:400;color:#b8bbd2;font-size:16px;top:68px}
.footer ul{list-style:none;top:109px;left:337px;font-size:12.5px}
.footer li{height:32px;display:flex;align-items:center;gap:10px}
.footer li::before{content:"";width:5px;height:5px;border-radius:50%;background:var(--white)}
.hours{left:611px;font-size:12.5px;display:flex;gap:14px;line-height:24px}
.social{left:890px;top:108px;display:flex;gap:14px}
.social span{width:30px;height:30px;border-radius:50%;border:1.5px solid var(--white)}
.social span.fill{background:var(--blue);border-color:var(--blue)}
.footer .rule{left:0;top:270px;width:1200px;height:1px;background:#3a3f72}
.footer .copy{left:0;width:1200px;top:281px;text-align:center;font-size:12.5px}
</style>
</head>
<body>

<div class="abs topbar">
  <div class="abs phone">
    <svg width="14" height="24" viewBox="0 0 14 24"><rect x="1" y="1" width="12" height="22" rx="2" fill="none" stroke="#fff" stroke-width="2"/><line x1="5" y1="19" x2="9" y2="19" stroke="#fff" stroke-width="1.5"/></svg>
    (555) 014-2290
  </div>
</div>

<header class="abs nav">
  <div class="abs brand"><span class="dot"></span>Gearhaven, LLC</div>
  <nav class="abs nav-links">
    <span style="left:389px">Home</span>
    <span style="left:477px">About Us</span>
    <span style="left:574px">Services</span>
    <span style="left:683px">Testimonials</span>
    <span style="left:794px">Contact Us</span>
  </nav>
  <div class="abs btn-light">Schedule A Service</div>
</header>

<section class="abs hero" role="img" aria-label="Photo of two mechanics working on a truck wheel in a workshop">
  <div class="abs shade"></div>
  <div class="abs kicker">SPECIALIZING IN VANTOR TRUCKS</div>
  <h1 class="abs">GEARHAVEN</h1>
  <p class="abs">Lorem Ipsum is simply dummy text of the printing and typesetting industry. Lorem Ipsum has been the industry's standard dummy text ever since the 1500s,</p>
  <div class="abs btn-light">Schedule A Service</div>
  <div class="abs arrow prev"><svg width="12" height="16" viewBox="0 0 12 16"><path d="M8 2 2 8l6 6" fill="none" stroke="#fff" stroke-width="2"/></svg></div>
  <div class="abs arrow next"><svg width="12" height="16" viewBox="0 0 12 16"><path d="M4 2l6 6-6 6" fill="none" stroke="#fff" stroke-width="2"/></svg></div>
</section>

<div class="abs band-pale"></div>

<article class="abs card" style="left:61px">
  <div class="icon"><svg width="48" height="48" viewBox="0 0 48 48" fill="none" stroke="#2d3b9c" stroke-width="2.5"><circle cx="20" cy="26" r="12" stroke-dasharray="5 3"/><circle cx="20" cy="26" r="5"/><path d="M32 8v30M28 8v6a4 4 0 0 0 8 0V8"/></svg></div>
  <h3>Repair</h3>
  <p>Lorem Ipsum is simply dummy text of the printing and typesetting industry. Lorem Ipsum has been the industry's standard dummy text.</p>
  <div class="more">Learn More <svg width="24" height="10" viewBox="0 0 24 10"><path d="M0 5h22M17 1l5 4-5 4" fill="none" stroke="currentColor" stroke-width="1.5"/></svg></div>
</article>
<article class="abs card active" style="left:430px">
  <div class="icon"><svg width="50" height="48" viewBox="0 0 50 48" fill="none" stroke="#fff" stroke-width="2.5"><rect x="6" y="8" width="22" height="28" rx="3"/><path d="M28 18h9l7 9v9H28"/><circle cx="13" cy="38" r="4"/><circle cx="36" cy="38" r="4"/></svg></div>
  <h3>Service</h3>
  <p>Lorem Ipsum is simply dummy text of the printing and typesetting industry. Lorem Ipsum has been the industry's standard dummy text.</p>
  <div class="more">Learn More <svg width="24" height="10" viewBox="0 0 24 10"><path d="M0 5h22M17 1l5 4-5 4" fill="none" stroke="currentColor" stroke-width="1.5"/></svg></div>
</article>
<article class="abs card" style="left:801px">
  <div class="icon"><svg width="48" height="48" viewBox="0 0 48 48" fill="none" stroke="#2d3b9c" stroke-width="2.5"><circle cx="24" cy="24" r="17" stroke-dasharray="6 3"/><path d="M16 32 32 16"/><circle cx="18" cy="18" r="3"/><circle cx="30" cy="30" r="3"/></svg></div>
  <h3>Sales</h3>
  <p>Lorem Ipsum is simply dummy text of the printing and typesetting industry. Lorem Ipsum has been the industry's standard dummy text.</p>
  <div class="more">Learn More <svg width="24" height="10" viewBox="0 0 24 10"><path d="M0 5h22M17 1l5 4-5 4" fill="none" stroke="currentColor" stroke-width="1.5"/></svg></div>
</article>

<section class="about">
  <div class="abs about-ring"></div>
  <div class="abs about-photo" role="img" aria-label="Photo of a smiling mechanic in blue overalls holding wrenches in front of an open car hood"></div>
  <h2 class="abs"><span class="l1">Welcome To</span><span class="l2">Gearhaven, LLC</span></h2>
  <p class="abs" style="top:1124px">Lorem Ipsum is simply dummy text of the printing and typesetting industry. Lorem Ipsum has been the industry's standard dummy text ever since the 1500s, when an unknown printer took a galley of type and scrambled it to make a type specimen book. It has survived not only five centuries, but also the leap into electronic typesetting, remaining essentially unchanged. It was popularised in the 1960s with the release of Letraset sheets containing Lorem Ipsum passages,</p>
  <p class="abs" style="top:1273px">It was popularised in the 1960s with the release of Letraset sheets containing Lorem Ipsum passages.</p>
  <div class="abs btn-blue">Learn More</div>
  <div class="abs or">OR</div>
  <div class="abs call"><svg width="20" height="36" viewBox="0 0 20 36"><rect x="1.5" y="1.5" width="17" height="33" rx="3" fill="none" stroke="#2d3b9c" stroke-width="2"/><line x1="7" y1="29" x2="13" y2="29" stroke="#2d3b9c" stroke-width="2"/></svg>(555) 014-2290</div>
</section>

<section class="abs cta">
  <h2 class="abs">Need Service For Your Truck Or Fleet?</h2>
  <p class="abs">Lorem Ipsum is simply dummy text of the printing and typesetting industry. Lorem Ipsum has been the industry's standard dummy text ever since the 1500s, when an unknown printer took a galley of type and scrambled it to make a type specimen book. It has survived not only five centuries, but also the leap into electronic typesetting.</p>
  <div class="abs req">Request A<br>Service</div>
</section>

<section class="abs reviews">
  <h2 class="abs">Customer <span>Reviews</span></h2>
  <div class="abs review" style="left:-17px;top:139px">
    <div class="stars"><svg width="90" height="14" viewBox="0 0 90 14" fill="#f3c316"><g id="s"><path d="M7 0l2 5h5l-4 3 2 5-5-3-5 3 2-5-4-3h5z"/></g><use href="#s" x="19"/><use href="#s" x="38"/><use href="#s" x="57"/><use href="#s" x="76"/></svg></div>
    <p>Lorem ipsum dolor sit amet, consectetur adipiscing elit, sed do eiusmod tempor incididunt ut labore et dolore magna aliqua.</p>
    <div class="who">Customer Name</div>
  </div>
  <div class="abs review" style="left:297px;top:112px">
    <div class="stars"><svg width="90" height="14" viewBox="0 0 90 14" fill="#f3c316"><use href="#s"/><use href="#s" x="19"/><use href="#s" x="38"/><use href="#s" x="57"/><use href="#s" x="76"/></svg></div>
    <p>Lorem ipsum dolor sit amet, consectetur adipiscing elit, sed do eiusmod tempor incididunt ut labore et dolore magna aliqua.</p>
    <div class="who">Customer Name</div>
  </div>
  <div class="abs review" style="left:611px;top:112px">
    <div class="stars"><svg width="90" height="14" viewBox="0 0 90 14" fill="#f3c316"><use href="#s"/><use href="#s" x="19"/><use href="#s" x="38"/><use href="#s" x="57"/><use href="#s" x="76"/></svg></div>
    <p>Lorem ipsum dolor sit amet, consectetur adipiscing elit, sed do eiusmod tempor incididunt ut labore et dolore magna aliqua.</p>
    <div class="who">Customer Name</div>
  </div>
  <div class="abs review" style="left:927px;top:139px">
    <div class="stars"><svg width="90" height="14" viewBox="0 0 90 14" fill="#f3c316"><use href="#s"/><use href="#s" x="19"/><use href="#s" x="38"/><use href="#s" x="57"/><use href="#s" x="76"/></svg></div>
    <p>Lorem ipsum dolor sit amet, consectetur adipiscing elit, sed do eiusmod tempor incididunt ut labore et dolore magna aliqua.</p>
    <div class="who">Customer Name</div>
  </div>
  <div class="abs pg" style="left:559px;background:#cfd0d8"><svg width="10" height="14" viewBox="0 0 10 14"><path d="M7 2 2 7l5 5" fill="none" stroke="#1c2154" stroke-width="1.6"/></svg></div>
  <div class="abs pg" style="left:607px;background:var(--blue)"><svg width="10" height="14" viewBox="0 0 10 14"><path d="M3 2l5 5-5 5" fill="none" stroke="#fff" stroke-width="1.6"/></svg></div>
</section>

<div class="abs map" role="img" aria-label="Street map showing the shop location at 412 Mill Yard Rd, Brookvale"></div>
<div class="abs contact-title"><span class="l1">we Love Talking</span><span class="l2">Gearhaven, LLC</span></div>

<section class="abs contact-box">
  <div class="abs info">
    <h4 class="abs">CONTACT INFO</h4>
    <div class="abs row" style="top:98px">
      <div class="ico"><svg width="14" height="18" viewBox="0 0 14 18"><path d="M7 17s6-6 6-10A6 6 0 0 0 1 7c0 4 6 10 6 10z" fill="none" stroke="#fff" stroke-width="1.4"/><circle cx="7" cy="7" r="2" fill="none" stroke="#fff" stroke-width="1.4"/></svg></div>
      <div><div class="lab">LOCATION</div><div class="val">412 Mill Yard Rd Brookvale,<br>NC 27000</div></div>
    </div>
    <div class="abs row" style="top:166px">
      <div class="ico"><svg width="18" height="18" viewBox="0 0 18 18"><path d="M4 1l3 4-2 2a10 10 0 0 0 6 6l2-2 4 3-2 3C8 17 1 10 1 3z" fill="none" stroke="#fff" stroke-width="1.4"/></svg></div>
      <div><div class="lab">CALL US</div><div class="val" style="font-weight:500">(555) 014-2290</div></div>
    </div>
    <div class="abs row" style="top:230px">
      <div class="ico"><svg width="18" height="14" viewBox="0 0 18 14"><rect x="1" y="1" width="16" height="12" rx="1" fill="none" stroke="#fff" stroke-width="1.4"/><path d="M1 2l8 6 8-6" fill="none" stroke="#fff" stroke-width="1.4"/></svg></div>
      <div><div class="lab">E-MAIL US</div><div class="val">hello@gearhavenautos.<br>com</div></div>
    </div>
  </div>
  <div class="form">
    <h4 class="abs">GET IN TOUCH</h4>
    <div class="abs field on" style="left:341px;top:73px;width:225px">First Name*</div>
    <div class="abs field" style="left:579px;top:73px;width:225px">Last Name*</div>
    <div class="abs field" style="left:341px;top:118px;width:225px">Phone No.*</div>
    <div class="abs field" style="left:579px;top:118px;width:225px">E-mail*</div>
    <div class="abs field" style="left:341px;top:161px;width:463px;height:113px">Massege*</div>
    <div class="abs btn-blue submit">Submit</div>
  </div>
</section>

<section class="abs callband">
  <h2 class="abs">Vantor Truck Service and Repair Call Now</h2>
  <div class="abs pill"><span class="c"><svg width="16" height="16" viewBox="0 0 18 18"><path d="M4 1l3 4-2 2a10 10 0 0 0 6 6l2-2 4 3-2 3C8 17 1 10 1 3z" fill="none" stroke="#2d3b9c" stroke-width="1.6"/></svg></span>(555) 014-2290</div>
</section>

<footer class="abs footer">
  <div class="abs brand"><span class="dot"></span>Gearhaven, LLC</div>
  <p class="abs blurb">Lorem Ipsum is simply dummy text of the printing and typesetting industry.</p>
  <h5 class="abs" style="left:337px">Site Map</h5>
  <ul class="abs"><li>Home</li><li>About Us</li><li>Services</li><li>Testimonials</li><li>Contact Us</li></ul>
  <h5 class="abs" style="left:615px">Hours</h5>
  <div class="abs hours" style="top:100px"><svg width="16" height="16" viewBox="0 0 16 16"><circle cx="8" cy="8" r="8" fill="#fff"/><path d="M8 4v4l3 2" stroke="#1c2154" stroke-width="1.6" fill="none"/></svg><div>Mon-Fri:<br>10:00AM To 5:00 PM</div></div>
  <div class="abs hours" style="top:152px"><svg width="16" height="16" viewBox="0 0 16 16"><circle cx="8" cy="8" r="8" fill="#fff"/><path d="M8 4v4l3 2" stroke="#1c2154" stroke-width="1.6" fill="none"/></svg><div>Sat:<br>By Appointment</div></div>
  <div class="abs hours" style="top:204px"><svg width="16" height="16" viewBox="0 0 16 16"><circle cx="8" cy="8" r="8" fill="#fff"/><path d="M8 4v4l3 2" stroke="#1c2154" stroke-width="1.6" fill="none"/></svg><div>Sun:<br>Closed</div></div>
  <h5 class="abs" style="left:890px">Follow On Us</h5>
  <div class="abs social"><span class="fill"></span><span></span><span></span></div>
  <div class="abs rule"></div>
  <div class="abs copy">Copyright ©&nbsp; 2022 GEARHAVEN, LLC.All rights reserved.</div>
</footer>

</body>
</html>
```